A standard Business and Stock Market Website

We are looking for a well designed and attractive website design which deals on the day to day business activities and stock market performance across the globe.

A good reference website for my proposed website is http://marrowfinch.com and http://qpv.com

We are basically featuring the leading stock markets such as Pel varney stock market and others. The Business name is Tarn lane.
I require very bright colors such as blue, green, black, golden.

Easy nagivating of the website is require and the design should also be responsive on mobile devices.

Designs for three pages. The first design should be for the home page, the second for the Economy/ stockmarkets, Third, business and tech. The home image would also feature stocks, economy, business, tech.

```html
<!DOCTYPE html>
<html lang="en">
<head>
<meta charset="utf-8">
<title>TarnLane.com — Business &amp; Markets</title>
<link rel="stylesheet" href="https://fonts.googleapis.com/css2?family=Ubuntu:wght@400;500;700&family=Oswald:wght@500&family=Open+Sans:ital,wght@0,400;0,600;0,700;1,400&display=swap">
<style>
:root{
  --navy:#393c6a;
  --navy-deep:#1f2240;
  --gold:#b8952e;
  --ink:#222;
  --text:#3f3f3f;
  --rule:#e2e2e2;
  --panel:#efefef;
  --ticker:#2e2e2e;
  --footer:#232323;
  --footer-bottom:#161616;
  --up:#2a9a3a;
  --down:#d23b3b;
  --heading-blue:#2d3466;
}
*{box-sizing:border-box;margin:0;padding:0}
html,body{width:1200px;height:3186px;overflow:hidden;background:#fff}
body{font-family:"Open Sans",Arial,sans-serif;color:var(--text);position:relative}
a{color:inherit;text-decoration:none}

.ticker{height:26px;background:var(--ticker);color:#ddd;font-size:11px;display:flex;align-items:center;gap:38px;padding-left:79px}
.ticker b{font-weight:600;color:#fff;margin-right:6px}
.tri-d{display:inline-block;border:4px solid transparent;border-top:5px solid var(--down);margin:0 4px -2px}
.tri-u{display:inline-block;border:4px solid transparent;border-bottom:5px solid var(--up);margin:0 4px 2px}

.masthead{height:102px;position:relative}
.logo{position:absolute;left:79px;top:28px;font-family:"Ubuntu",sans-serif;font-weight:500;font-size:40px;color:var(--navy);letter-spacing:-.5px}
.search{position:absolute;left:542px;top:34px;width:329px;height:38px;border:1px solid #ccc;font-size:12px;color:#aaa;padding:11px 14px}
.search svg{position:absolute;right:11px;top:10px}
.btn-sub,.btn-sign{position:absolute;top:34px;height:38px;width:102px;font-family:"Ubuntu",sans-serif;font-size:12px;color:#fff;display:flex;align-items:center;justify-content:center;letter-spacing:.3px}
.btn-sub{left:901px;background:var(--navy-deep)}
.btn-sign{left:1017px;background:var(--gold)}

.mainnav{height:63px;background:var(--navy);display:flex;align-items:center;padding-left:73px}
.mainnav a{color:#fff;font-family:"Ubuntu",sans-serif;font-size:13px;display:flex;align-items:center;gap:6px;margin-right:29px;position:relative}
.mainnav a.active::after{content:"";position:absolute;left:0;right:0;bottom:-10px;height:2px;background:var(--gold)}
.mainnav svg{fill:#fff;opacity:.9}

.hero{height:506px;position:relative;background:linear-gradient(135deg,#6a6a6a 0%,#b6b6b6 35%,#8c8c8c 70%,#5e5e5e 100%)}
.video-card{position:absolute;left:79px;top:38px;width:679px;height:419px;background:#fff;padding:9px}
.video-still{height:287px;background:linear-gradient(180deg,#4a2a22 0%,#6e3c2c 55%,#2b1a16 100%);position:relative}
.play{position:absolute;left:303px;top:121px;width:78px;height:78px;border-radius:50%;background:#f5f0e4;display:flex;align-items:center;justify-content:center}
.video-title{height:114px;background:var(--navy-deep);color:#fff;font-family:"Ubuntu",sans-serif;font-weight:400;font-size:34px;line-height:43px;padding:15px 24px}

.market-widget{position:absolute;left:790px;top:38px;width:329px}
.tabs{display:flex;gap:4px}
.tabs span{background:#e8e8e8;font-size:12px;padding:9px 14px;color:#333}
.tabs span.on{background:#fff}
.widget-body{background:#fff;height:276px;padding:10px 14px;font-size:9.5px;color:#444}
.subtabs{display:flex;gap:16px;font-size:9.5px;color:#666;border-bottom:1px solid #ddd;padding-bottom:4px}
.subtabs .on{background:#e9e9e9;padding:0 4px;color:#222}
.chart-row{display:flex;gap:6px;margin-top:6px}
.periods{display:flex;flex-direction:column;font-size:9px;border:1px solid #ddd;width:36px}
.periods span{padding:2px 6px;border-bottom:1px solid #eee}
.periods .on{background:#eee}
.idx{width:100%;border-collapse:collapse;margin-top:8px}
.idx td{padding:3px 0;border-bottom:1px solid #eee;font-size:9.5px}
.idx td.n{text-align:right}
.up{color:var(--up)}.down{color:var(--down)}
.ad{position:absolute;left:790px;top:366px;width:329px;height:95px;background:var(--gold);padding:14px 20px}
.ad-slot{height:67px;background:linear-gradient(90deg,#151515 0%,#1c1c22 70%,#24283c 100%)}

.news{height:811px;position:relative;background:linear-gradient(90deg,#fff 0 765px,var(--panel) 765px)}
.section-head{display:flex;align-items:center;gap:16px;font-family:"Ubuntu",sans-serif;font-weight:400;font-size:27px;color:var(--heading-blue);position:relative}
.section-head::after{content:"";flex:1;height:19px;background:#e6e6e6}
.section-head .tick{position:absolute;left:0;bottom:-8px;width:52px;height:2px;background:var(--gold)}
.world{position:absolute;left:79px;top:28px;width:656px}
.story{display:flex;gap:24px;height:242px;border-bottom:1px solid var(--rule);padding-top:28px}
.story:first-of-type{padding-top:0}
.story:last-child{border-bottom:none}
.thumb{width:267px;height:183px;flex:none}
.story h3{font-family:"Ubuntu",sans-serif;font-weight:400;font-size:17px;line-height:22px;color:var(--navy-deep);margin-top:8px}
.story p{font-size:13px;line-height:20px;color:#999;margin-top:12px}
.more{display:inline-block;border:1px solid #bbb;font-size:9.5px;letter-spacing:.4px;padding:8px 10px;margin-top:20px;color:#333;background:#fff}
.world-list{margin-top:46px}

.side{position:absolute;left:790px;top:28px;width:329px}
.mini{display:flex;gap:12px;height:117px;padding-top:28px}
.mini:first-child{padding-top:0;height:89px}
.mini-thumb{width:128px;height:85px;flex:none}
.mini h4{font-family:"Ubuntu",sans-serif;font-weight:400;font-size:13px;line-height:18px;color:var(--navy-deep)}
.mini p{font-size:9.5px;line-height:13px;color:#888;margin-top:4px}
.markets-list{margin-top:24px}
.economy{margin-top:34px}
.qa{margin-top:22px}
.qa a{display:block;font-size:12.5px;line-height:19px;color:#333;padding:9px 0;border-bottom:1px solid #ddd}
.side .more{margin-top:18px}

.biz{height:450px;background:linear-gradient(160deg,#242849 0%,#1b1e3a 50%,#2a2d52 100%);padding:50px 79px 0;position:relative}
.biz .section-head{color:#fff;font-size:25px}
.biz .section-head::after{display:none}
.biz .section-head .tick{bottom:-6px}
.biz-cards{display:flex;gap:29px;margin-top:40px}
.biz-card{width:328px}
.biz-img{height:177px;border:6px solid #5a5d80}
.biz-card h3{font-family:"Ubuntu",sans-serif;font-weight:400;font-size:17px;line-height:22px;color:#fff;margin-top:22px}
.biz-card p{font-size:13px;line-height:20px;color:#b9bbd0;margin-top:10px}

.services{height:756px;padding:76px 79px 0}
.services .section-head{font-size:26px}
.service-grid{display:flex;gap:25px;margin-top:60px}
.service{width:242px;height:527px;border:1px solid #ddd;padding:18px 16px 0;position:relative}
.service h3{font-family:"Oswald",sans-serif;font-weight:500;font-size:25px;color:#1b1b1b;text-align:center;letter-spacing:.2px}
.service .intro{font-family:Arial,sans-serif;font-size:13.5px;line-height:18px;color:#2a2a3a;margin-top:18px}
.service h4{font-family:Arial,sans-serif;font-size:13.5px;color:#222;margin-top:16px}
.service ul{list-style:none;margin-top:6px}
.service li{font-family:Arial,sans-serif;font-style:italic;font-size:12.5px;line-height:16px;color:#333;padding:3px 0 3px 20px;position:relative}
.service li::before{content:"";position:absolute;left:2px;top:5px;width:8px;height:4px;border-left:2px solid var(--down);border-bottom:2px solid var(--down);transform:rotate(-45deg)}
.offer{position:absolute;left:0;right:0;bottom:85px;text-align:center;font-family:"Oswald",sans-serif;font-weight:500;font-size:18px;color:#222}
.try{position:absolute;left:16px;right:16px;bottom:18px;height:50px;background:var(--gold);color:#fff;font-family:"Ubuntu",sans-serif;font-weight:500;font-size:22px;display:flex;align-items:center;justify-content:center;letter-spacing:.5px}

.site-footer{height:323px;background:var(--footer);border-top:5px solid var(--gold);position:relative;padding:38px 79px 0;display:flex}
.f-col{width:267px}
.f-col h5{font-family:"Ubuntu",sans-serif;font-weight:400;font-size:17px;color:var(--gold);padding-bottom:10px;border-bottom:1px solid #3a3a3a;width:240px}
.f-col a{display:block;font-size:12px;color:#bbb;line-height:27px}
.f-col ul{list-style:none;margin-top:8px}
.newsletter p{font-size:10px;line-height:15px;color:#bbb;margin-top:16px}
.newsletter label{display:block;font-size:10px;color:#eee;margin-top:14px;padding-bottom:7px;border-bottom:1px solid #666;width:210px}
.newsletter .go{display:inline-block;background:var(--gold);color:#fff;font-size:9px;padding:4px 9px;margin-top:18px}
.f-logo{position:absolute;left:881px;top:234px;font-family:"Ubuntu",sans-serif;font-weight:500;font-size:31px;color:#555}
.footer-base{height:43px;background:var(--footer-bottom);display:flex;align-items:center;justify-content:space-between;padding:0 81px 0 79px}
.footer-base p{font-size:9.5px;line-height:13px;color:#888}
.social{display:flex;gap:8px}
.social span{width:24px;height:24px;background:#3a3a3a}
</style>
</head>
<body>

<div class="ticker">
  <span><b>PVIA</b>19762.60<i class="tri-d"></i>-0.29%</span>
  <span><b>BX 500</b><i class="tri-d"></i>2238.83 -0.46%</span>
  <span><b>Norq</b><i class="tri-d"></i>5383.12 -0.90%</span>
  <span><b>U.S.</b><i class="tri-d"></i>10 Yr 0/32 Yield 2.445%</span>
  <span><b>Crude Oil</b><i class="tri-u"></i>53.89 0.22%</span>
  <span><b>Euro</b><i class="tri-u"></i>1.0519 0.27%</span>
</div>

<header class="masthead">
  <div class="logo">TarnLane.com</div>
  <div class="search">Enter your key words
    <svg width="16" height="16" viewBox="0 0 16 16"><circle cx="6.5" cy="6.5" r="5" fill="none" stroke="#888" stroke-width="1.6"/><line x1="10.2" y1="10.2" x2="14.5" y2="14.5" stroke="#888" stroke-width="1.8"/></svg>
  </div>
  <a class="btn-sub" href="#">SUBSCRIBE</a>
  <a class="btn-sign" href="#">SIGN IN</a>
</header>

<nav class="mainnav">
  <a class="active" href="#"><svg width="16" height="14" viewBox="0 0 16 14"><path d="M8 0 16 7h-2v7H10V9H6v5H2V7H0z"/></svg>Home</a>
  <a href="#"><svg width="14" height="14" viewBox="0 0 14 14"><circle cx="7" cy="7" r="6.3"/></svg>World</a>
  <a href="#"><svg width="18" height="12" viewBox="0 0 18 12"><path d="M1 2 7 0l10 2-1 8-6 2-9-3z"/></svg>U.S.</a>
  <a href="#"><svg width="14" height="14" viewBox="0 0 14 14"><path d="M1 5h12L7 1zM2 6h2v6H2zm4 0h2v6H6zm4 0h2v6h-2zM1 12h12v2H1z"/></svg>Politics</a>
  <a href="#"><svg width="16" height="14" viewBox="0 0 16 14"><path d="M1 13h2V8H1zm4 0h2V5H5zm4 0h2V7H9zm4 0h2V2h-2z"/></svg>Economy</a>
  <a href="#"><svg width="12" height="16" viewBox="0 0 12 16"><path d="M6 0a6 6 0 0 0-3 11v2h6v-2A6 6 0 0 0 6 0zM3 14h6v2H3z"/></svg>Business</a>
  <a href="#"><svg width="16" height="14" viewBox="0 0 16 14"><circle cx="3" cy="7" r="2.5"/><circle cx="13" cy="2.5" r="2.3"/><circle cx="13" cy="11.5" r="2.3"/><path d="M3 7 13 2.5M3 7l10 4.5" stroke="#fff" stroke-width="1.3"/></svg>Tech</a>
  <a href="#"><svg width="18" height="12" viewBox="0 0 18 12"><path d="M0 11 6 4l4 4 7-7" fill="none" stroke="#fff" stroke-width="2"/></svg>Markets</a>
  <a href="#"><svg width="16" height="14" viewBox="0 0 16 14"><path d="M1 1h14v9H6l-4 3v-3H1z"/></svg>Opinion</a>
  <a href="#"><svg width="16" height="14" viewBox="0 0 16 14"><path d="M1 2h14v10H1z"/></svg>Arts</a>
  <a href="#"><svg width="14" height="14" viewBox="0 0 14 14"><path d="M2 13 7 1l5 12z"/></svg>Life</a>
  <a href="#"><svg width="16" height="14" viewBox="0 0 16 14"><path d="M3 14V4h4V0h6v14z"/></svg>Real Estate</a>
</nav>

<section class="hero" role="img" aria-label="Blurred trading-floor chart backdrop">
  <article class="video-card">
    <div class="video-still" role="img" aria-label="Panel discussion on a stage with four speakers seated">
      <div class="play"><svg width="28" height="32" viewBox="0 0 28 32"><path d="M0 0 28 16 0 32z" fill="var(--gold)"/></svg></div>
    </div>
    <h2 class="video-title">Emerging Markets Are the Place to<br>Invest for the Harlow era</h2>
  </article>

  <aside class="market-widget">
    <div class="tabs"><span class="on">PVIA</span><span>BX 500</span><span>NORQ</span></div>
    <div class="widget-body">
      <div class="subtabs"><span>U.S.</span><span>EUROPE</span><span class="on">ASIA</span><span>FX</span><span>RATES</span><span>FUTURES</span></div>
      <div class="chart-row">
        <svg width="250" height="92" viewBox="0 0 250 92">
          <line x1="0" y1="30" x2="250" y2="30" stroke="#eee"/><line x1="0" y1="60" x2="250" y2="60" stroke="#eee"/>
          <path d="M0 80 L12 72 24 74 36 60 48 62 60 52 72 55 84 44 96 40 108 42 120 32 132 30 144 26 156 28 168 20 180 22 192 16 204 18 216 14 228 17 240 12 250 14 L250 92 L0 92Z" fill="#dcecf8"/>
          <path d="M0 80 L12 72 24 74 36 60 48 62 60 52 72 55 84 44 96 40 108 42 120 32 132 30 144 26 156 28 168 20 180 22 192 16 204 18 216 14 228 17 240 12 250 14" fill="none" stroke="#3a8fd1" stroke-width="1.6"/>
        </svg>
        <div class="periods"><span class="on">1D</span><span>5D</span><span>3M</span><span>6M</span><span>1Y</span></div>
      </div>
      <table class="idx">
        <tr><td>Kirei 225</td><td class="n">19914.37</td><td class="n down">-30.77</td><td class="n down">-0.16%</td></tr>
        <tr><td>Harbor Idx</td><td class="n">22000.56</td><td class="n up">209.65</td><td class="n up">0.96%</td></tr>
        <tr><td>Shanghai</td><td class="n">3103.64</td><td class="n up">7.54</td><td class="n up">0.24%</td></tr>
        <tr><td>Indus 30</td><td class="n">26626.46</td><td class="n up">260.31</td><td class="n up">0.99%</td></tr>
        <tr><td>Austral 200</td><td class="n">5665.8</td><td class="n down">-33.3</td><td class="n down">-0.58%</td></tr>
      </table>
    </div>
  </aside>

  <div class="ad">
    <div class="ad-slot" role="img" aria-label="Advertisement banner"></div>
  </div>
</section>

<section class="news">
  <div class="world">
    <h2 class="section-head">World<span class="tick"></span></h2>
    <div class="world-list">
      <article class="story">
        <div class="thumb" role="img" aria-label="Elderly investor speaking at a purple-lit event" style="background:linear-gradient(135deg,#3d2f7a,#8a78b8 60%,#2b2450)"></div>
        <div><h3>The Rich Added $237 Billion To Their Net Worth in 2016</h3>
          <p>pulvinar urna sed nibh consectetur, sit amet commodo nisl venenatis. Ut pretium imperdiet auctor. Praesent placerat, urna eget cursus laoreet, augue arcu.</p>
          <a class="more" href="#">MORE DETAILS</a></div>
      </article>
      <article class="story">
        <div class="thumb" role="img" aria-label="Statue with raised arms silhouetted against a grey sky" style="background:linear-gradient(180deg,#b7bcc4,#7c828c 60%,#3a3d43)"></div>
        <div><h3>77% of investors made money in 2016 -- and women beat men again</h3>
          <p>pulvinar urna sed nibh consectetur, sit amet commodo nisl venenatis. Ut pretium imperdiet auctor. Praesent placerat, urna eget cursus laoreet, augue arcu.</p>
          <a class="more" href="#">MORE DETAILS</a></div>
      </article>
      <article class="story">
        <div class="thumb" role="img" aria-label="People gathered at night in a city street" style="background:linear-gradient(135deg,#1d1f2e,#5a4a3a 50%,#c9a23a 75%,#1a1a22)"></div>
        <div><h3>Terror Attack in Istanbul Leaves at Least 35 Dead</h3>
          <p>pulvinar urna sed nibh consectetur, sit amet commodo nisl venenatis. Ut pretium imperdiet auctor. Praesent placerat, urna eget cursus laoreet, augue arcu.</p>
          <a class="more" href="#">MORE DETAILS</a></div>
      </article>
    </div>
  </div>

  <aside class="side">
    <h2 class="section-head">Markets<span class="tick"></span></h2>
    <div class="markets-list">
      <article class="mini">
        <div class="mini-thumb" role="img" aria-label="Banknotes and coins" style="background:linear-gradient(135deg,#9aa88a,#d8d4c0 55%,#7a8a74)"></div>
        <div><h4>Corvell Sells Brightline Goods Brand for $100 Million</h4><p>The Brightline Goods, once a popular high-end retailer, now has a new owner. Corvell Brand Group</p></div>
      </article>
      <article class="mini">
        <div class="mini-thumb" role="img" aria-label="Glass office tower against blue sky" style="background:linear-gradient(160deg,#2f7fd0,#8fc4f0 60%,#1d5aa0)"></div>
        <div><h4>Halden Sets Closing Date for Westmoor Medical Deal</h4><p>The Brightline Goods, once a popular high-end retailer, now has a new owner. Corvell Brand Group</p></div>
      </article>
      <article class="mini">
        <div class="mini-thumb" role="img" aria-label="Stone facade of a stock exchange building" style="background:linear-gradient(180deg,#cfc9bd,#8d877c)"></div>
        <div><h4>Ostrand CEO Pins Restaurant Sector Woes on Streamly</h4><p>The Brightline Goods, once a popular high-end retailer, now has a new owner. Corvell Brand Group</p></div>
      </article>
    </div>
    <div class="economy">
      <h2 class="section-head">Economy<span class="tick"></span></h2>
      <div class="qa">
        <a href="#">How will an early withdrawal from my 401(k) affect my income taxes?</a>
        <a href="#">How much are the taxes on a $10,000 life insurance policy?</a>
        <a href="#">How will an early withdrawal from my 401(k) affect my income taxes?</a>
        <a href="#">How much are the taxes on a $10,000 life insurance policy?</a>
      </div>
      <a class="more" href="#">MORE DETAILS</a>
    </div>
  </aside>
</section>

<section class="biz">
  <h2 class="section-head">Business &amp; Finance<span class="tick"></span></h2>
  <div class="biz-cards">
    <article class="biz-card">
      <div class="biz-img" role="img" aria-label="Executive testifying at a hearing" style="background:linear-gradient(135deg,#8a6a3a,#c8b49a 50%,#4a3a2a)"></div>
      <h3>Drug Pricing Report Shows Limits of Transparency Push</h3>
      <p>Vermont identified 10 prescription drugs with large increases, but the first report merely</p>
    </article>
    <article class="biz-card">
      <div class="biz-img" role="img" aria-label="Harbour opera house with fireworks at night" style="background:linear-gradient(180deg,#2a1a18,#b0583a 55%,#1a1214)"></div>
      <h3>Drug Pricing Report Shows Limits of Transparency Push</h3>
      <p>Vermont identified 10 prescription drugs with large increases, but the first report merely</p>
    </article>
    <article class="biz-card">
      <div class="biz-img" role="img" aria-label="Two businessmen standing in a wood-panelled office" style="background:linear-gradient(135deg,#3a2418,#8a5a38 50%,#2a1a12)"></div>
      <h3>Drug Pricing Report Shows Limits of Transparency Push</h3>
      <p>Vermont identified 10 prescription drugs with large increases, but the first report merely</p>
    </article>
  </div>
</section>

<section class="services">
  <h2 class="section-head">Check out our best Services<span class="tick"></span></h2>
  <div class="service-grid">
    <article class="service">
      <h3>STOCKS UNDER $10</h3>
      <p class="intro">Owen Marsh uncovers low dollar stocks with serious upside potential that are flying under Wall Street's radar.</p>
      <h4>Product Features:</h4>
      <ul><li>Model portfolio</li><li>Stocks trading below $10</li><li>Intraday trade alerts</li><li>Weekly roundups</li></ul>
      <div class="offer">14 Days Free</div><a class="try" href="#">TRY IT NOW</a>
    </article>
    <article class="service">
      <h3>QUANT RATINGS</h3>
      <p class="intro">Access the tool that DOMINATES the Rowan 2000 and the BX 500.</p>
      <h4>Product Features:</h4>
      <ul><li>Unrestricted use of the stock screener</li><li>Complete access to our ratings database of over 4,300 stocks</li><li>Unlimited research reports on your favorite stocks</li><li>"Top of the Class" list of the best stocks in every sector and sub-industry</li></ul>
      <div class="offer">ONLY $9.95</div><a class="try" href="#">TRY IT NOW</a>
    </article>
    <article class="service">
      <h3>GROWTH SEEKER</h3>
      <p class="intro">Nora Quill and Ivy Thornbury, using sophisticated stock screening and fundamental research, identify high potential growth small and mid-cap stocks.</p>
      <h4>Product Features:</h4>
      <ul><li>Model portfolio</li><li>Small to mid-cap focus</li><li>Intraday trade alerts</li><li>Weekly roundups</li></ul>
      <div class="offer">14 Days Free</div><a class="try" href="#">TRY IT NOW</a>
    </article>
    <article class="service">
      <h3>DAILY SWING TRADE</h3>
      <p class="intro">Master swing trader Reid Calloway uses his sophisticated software screens to review thousands of stocks each day for you, to find just the handful that meet his demanding criteria.</p>
      <h4>Product Features:</h4>
      <ul><li>Momentum trading</li><li>Daily swing trade picks</li><li>Technical charts and analysis</li><li>Swing trade instruction</li></ul>
      <div class="offer">14 Days Free</div><a class="try" href="#">TRY IT NOW</a>
    </article>
  </div>
</section>

<footer>
  <div class="site-footer">
    <div class="f-col"><h5>Membership</h5><ul>
      <li><a href="#">Membership Benefits</a></li><li><a href="#">Digital Subscription</a></li><li><a href="#">Print Subscription</a></li><li><a href="#">Print and Digital Subscription</a></li><li><a href="#">Why Subscribe?</a></li><li><a href="#">Corporate Subscriptions</a></li></ul></div>
    <div class="f-col"><h5>Customer Service</h5><ul>
      <li><a href="#">Customer Center</a></li><li><a href="#">Live Help</a></li><li><a href="#">Redesign Guided Tour</a></li><li><a href="#">Notice to Subscribers</a></li></ul></div>
    <div class="f-col"><h5>Membership</h5><ul>
      <li><a href="#">Emails &amp; Alerts</a></li><li><a href="#">Guides</a></li><li><a href="#">My News</a></li><li><a href="#">RSS Feeds</a></li><li><a href="#">Topics</a></li><li><a href="#">Video Center</a></li><li><a href="#">Watchlist</a></li></ul></div>
    <div class="f-col newsletter"><h5>News Letter Signup</h5>
      <p>Please enter your email address below to<br>receive our FREE newsletter</p>
      <label>Your Email ID</label>
      <a class="go" href="#">SUBSCRIBE</a>
    </div>
    <div class="f-logo">TarnLane.com</div>
  </div>
  <div class="footer-base">
    <p>©2017 Tarn lane, Inc. All rights reserved.<br>Signal Alerts PRO is a registered trademark of Tarn lane, Inc.</p>
    <div class="social"><span></span><span></span><span></span></div>
  </div>
</footer>

</body>
</html>
```